Brasolina! Poster

I need a poster for an event to be staged in Gibraltar called Brasolina!
Brasolina! is a food festival and street party that celebrates GIbraltar's multicultural and colour community. The event has a tagline "Flavours of the Warm Bowl".
I am looking for a poster which captures the spirit of the event without being too obvious.
Updates

Because this event is rapidly approaching I would like to settle the design for the poster as soon as possible, so the earlier you post the better
thanks

I am trying to avoid a poster that looks too similar to last year's.
Red and White are Gibraltar's national colours and I would like to feature them in the design.
Brasolina! the name needs to be in Clarendon! (bold) with tight character spacing

Target Market(s)

Target market are the people of Gibraltar - Gibraltar is a british colony in southern Spain, population 30,000 - Gibraltarians are of British, Spanish, Italian (Genoa), Portugese and Moroccan extraction. Gibraltar also has large Hindu, Jewish and Moroccan Communities.

Industry/Entity Type

Events

Requirements
Must have
• Initially I am looking for an A2 design - we will use the same design themes for the website and also base a 120cm x 90cm banner on the design.
• Must have t
• "HearsayStagesLive.com" "Brasolina!" , "Flavours of the Warm Bowl", Friday June 19th 2009, Ropewalk Plaza, Starts 21.00 hrs Finishes 0100 hrs, Free Entry, Everyone Welcome, Firework and Laser Display at 22.30 hrs
• My company logo, Office of Heritage Bloom Fair Logo
• Title must use Clarendon font
Nice to have
• Could be a photo or an illustration nothing that too obviously reflects the theme, doesn''t need to have all or anymore than one of the main Gibraltarian cultures
Should not have
• picture of the ROck of Gibaltar, Money, bad photography in particular bad food photography, just a picture of some food

```html
<!DOCTYPE html>
<html lang="en">
<head>
<meta charset="utf-8">
<title>Brasolina! – Flavours of the Warm Bowl</title>
<link rel="stylesheet" href="https://fonts.googleapis.com/css2?family=Alfa+Slab+One&family=Rokkitt:wght@700&family=Cabin:wght@400;600;700&display=swap">
<style>
  :root {
    --paper: #f5f0e0;
    --paper-edge: #8a6a55;
    --red: #d2232e;
    --red-deep: #9e1b22;
    --brown: #3d2a22;
    --strip: #f7f4ee;
    --tile-blue: #8fb0c0;
    --badge: #5a78b4;
  }
  * { margin: 0; padding: 0; box-sizing: border-box; }
  html, body { width: 849px; height: 1200px; overflow: hidden; background: var(--paper); }
  .poster {
    position: relative;
    width: 849px;
    height: 1200px;
    background: radial-gradient(ellipse at 50% 45%, #faf6ea 0%, var(--paper) 70%, #ece3cc 100%);
    box-shadow: inset 0 0 0 6px rgba(138,106,85,.55), inset 0 0 30px 8px rgba(138,106,85,.45);
    font-family: "Cabin", "Gill Sans", sans-serif;
    color: var(--brown);
    overflow: hidden;
  }
  .flourish {
    position: absolute;
    left: 28px; top: 64px;
    width: 812px; height: 440px;
    border-radius: 48% 48% 40% 40%;
    background: radial-gradient(ellipse at 50% 45%, rgba(210,35,46,0) 55%, rgba(210,35,46,.16) 72%, rgba(210,35,46,0) 90%);
  }
  .site-url {
    position: absolute;
    top: 62px; left: 0; width: 100%;
    text-align: center;
    font-size: 19px;
    letter-spacing: .1px;
    color: var(--brown);
  }
  .title-art, .tagline-art, .collage {
    position: absolute;
    left: 0; top: 0;
  }
  .title-word {
    font-family: "Alfa Slab One", "Clarendon", serif;
  }
  .tagline-word {
    font-family: "Rokkitt", "Clarendon", serif;
    font-weight: 700;
  }
  .event-details {
    position: absolute;
    top: 808px; left: 0; width: 100%;
    text-align: center;
    font-size: 23px;
    line-height: 31px;
    letter-spacing: 3px;
    text-transform: uppercase;
  }
  .event-details p + p { margin-top: 31px; }
  .partners {
    position: absolute;
    top: 1100px; left: 0; width: 100%; height: 90px;
  }
  .festival-credit {
    position: absolute;
    left: 180px; top: 30px;
    width: 154px;
    text-align: right;
    font-size: 8.5px;
    line-height: 11px;
  }
  .credit-label {
    display: block;
    font-weight: 700;
    font-size: 6px;
    letter-spacing: .4px;
    text-transform: uppercase;
  }
  .festival-badge {
    position: absolute;
    left: 339px; top: 23px;
    width: 77px; height: 57px;
    background: var(--badge);
  }
  .promoter-mark {
    position: absolute;
    left: 426px; top: 37px;
    width: 76px;
    display: flex; align-items: center; gap: 3px;
    font-size: 5.5px;
    font-weight: 600;
    letter-spacing: .5px;
    white-space: nowrap;
    text-transform: uppercase;
  }
  .promoter-dot {
    flex: none;
    width: 6px; height: 6px;
    border-radius: 50%;
    background: var(--brown);
  }
  .organiser-credit {
    position: absolute;
    left: 507px; top: 30px;
    font-size: 8.5px;
    line-height: 11px;
    white-space: nowrap;
  }
</style>
</head>
<body>
<main class="poster">
  <div class="flourish" role="img" aria-label="Red scrolling flourish ornament framing the title"></div>

  <p class="site-url">HearsayStagesLive.com</p>

  <svg class="title-art" width="849" height="280" viewBox="0 0 849 280" aria-labelledby="event-title">
    <rect x="68" y="140" width="731" height="126" fill="var(--strip)" transform="rotate(-0.6 433 203)"/>
    <text id="event-title" class="title-word" x="80" y="262" font-size="132" letter-spacing="-4"
          textLength="718" lengthAdjust="spacingAndGlyphs" fill="var(--brown)">Brasolina!</text>
    <text class="title-word" x="75" y="256" font-size="132" letter-spacing="-4"
          textLength="718" lengthAdjust="spacingAndGlyphs" fill="var(--red)" aria-hidden="true">Brasolina!</text>
  </svg>

  <svg class="tagline-art" width="849" height="340" viewBox="0 0 849 340" aria-label="Flavours of the Warm Bowl">
    <rect x="308" y="286" width="441" height="42" fill="var(--strip)" stroke="#d9d2c4" stroke-width="1" transform="rotate(-0.8 528 307)"/>
    <text class="tagline-word" x="528" y="316" font-size="25" text-anchor="middle"
          textLength="390" lengthAdjust="spacingAndGlyphs" fill="var(--brown)">Flavours of the Warm Bowl</text>
  </svg>

  <svg class="collage" width="849" height="760" viewBox="0 0 849 760" role="img"
       aria-label="Cloud-shaped collage of red damask, floral print and blue Mediterranean tiles">
    <defs>
      <linearGradient id="collage-fill" x1="0" y1="0" x2="1" y2="1">
        <stop offset="0" stop-color="var(--tile-blue)"/>
        <stop offset=".35" stop-color="var(--red-deep)"/>
        <stop offset=".7" stop-color="#b8404a"/>
        <stop offset="1" stop-color="#7ea0b4"/>
      </linearGradient>
    </defs>
    <g fill="url(#collage-fill)">
      <circle cx="180" cy="520" r="70"/>
      <circle cx="125" cy="595" r="32"/>
      <circle cx="240" cy="665" r="78"/>
      <circle cx="350" cy="420" r="90"/>
      <circle cx="440" cy="410" r="75"/>
      <circle cx="390" cy="560" r="130"/>
      <circle cx="430" cy="665" r="78"/>
      <circle cx="560" cy="490" r="78"/>
      <circle cx="625" cy="505" r="80"/>
      <circle cx="610" cy="650" r="80"/>
      <circle cx="655" cy="660" r="55"/>
    </g>
  </svg>

  <section class="event-details">
    <p>Friday June 19th 2009<br>21.00 hrs - 01.00 hrs<br>Ropewalk Plaza</p>
    <p>Free Entry<br>Everyone Welcome<br>Firework and Laser Display 22.30 hrs</p>
  </section>

  <footer class="partners">
    <p class="festival-credit"><span class="credit-label">A part of</span>The Office of Heritage Bloom Fair</p>
    <div class="festival-badge" role="img" aria-label="Partner festival badge"></div>
    <p class="promoter-mark"><span class="promoter-dot"></span>Hearsay Stages</p>
    <p class="organiser-credit"><span class="credit-label">Organised by</span>Hearsay Stages</p>
  </footer>
</main>
</body>
</html>
```